'Orla Property Development' Business Card

Business Card Features:

High Quality (potentially textured) thick card - preference is white textured card

Logo (supplied)

We plan to use the vertical logo as the main logo. But i am happy for people to use either if they find it works better for the design of the card.

The building icon and also the insert to the 'E' is in a metallic finish, i think this should be finished in a metallic embossed or raised style.
Updates

Please note i have attached both a horizontal and Vertical Logo for your reference. We plan to use the vertical logo as the main logo. But i am happy for people to use either if they find it works better for the design of the card.

Please note i am considering having the cards made on stainless steel. This introduces the option of having cut outs in the card and etching or printing for the design. If you have a good concept for this please submit.

http://www.quorvantprint.co.uk/black-metal-cards# this is a site that makes the metal cards to offer some direction . . . . Please note i am basic the selection o the best design, if that means normal print cards on paper then this is what i will choose. But there are some great options with the metal. Thanks.

Industry/Entity Type

Building

Requirements
Must have
• Helvetica font to details side of card - logo as supplied to opposite side.

Card Details:

Darren Ashcombe
Managing Director

+61 438 615 207
+61 3 8276 4139

PO Box 73
Bentleigh, VIC 3024

darren@orla.properties

www.orla.properties

```html
<!DOCTYPE html>
<html lang="en">
<head>
<meta charset="utf-8">
<title>Orla Property Development – Business Card</title>
<link href="https://fonts.googleapis.com/css2?family=Arimo:wght@400;700&display=swap" rel="stylesheet">
<style>
  :root {
    --backdrop: #1c1c1d;
    --card-dark: #141415;
    --card-mid: #232325;
    --card-light: #2c2c2e;
    --card-edge: #3a3a3c;
    --text-main: #a9abae;
    --text-soft: #8c8e91;
    --metal: #b9bcc0;
  }
  * { box-sizing: border-box; margin: 0; padding: 0; }
  html, body {
    width: 1200px; height: 849px; overflow: hidden;
    background: var(--backdrop);
    font-family: "Arimo", "Helvetica Neue", Helvetica, Arial, sans-serif;
  }
  .canvas {
    position: relative; width: 1200px; height: 849px;
    display: flex; align-items: center; justify-content: center;
  }
  .card {
    position: relative; width: 900px; height: 568px;
    border-radius: 26px;
    border: 1px solid var(--card-edge);
    background:
      repeating-linear-gradient(0deg, rgba(255,255,255,0.018) 0 1px, transparent 1px 3px),
      linear-gradient(160deg, var(--card-light) 0%, var(--card-mid) 40%, var(--card-dark) 100%);
    box-shadow: 0 20px 50px rgba(0,0,0,0.55);
  }
  .brand {
    position: absolute; left: 70px; top: 180px; width: 370px;
    display: flex; flex-direction: column; align-items: center; gap: 22px;
    text-align: center;
  }
  .brand-mark {
    width: 70px; height: 70px; background: var(--metal);
  }
  .brand-name {
    color: var(--metal); font-size: 34px; font-weight: 700; letter-spacing: 0.5px;
    line-height: 1.2;
  }
  .details {
    position: absolute; left: 500px; top: 60px; width: 370px; color: var(--text-main);
  }
  .person-name { font-size: 34px; font-weight: 400; }
  .person-role {
    font-size: 19px; text-transform: uppercase; color: var(--text-soft);
    letter-spacing: 0.5px; margin-top: 4px;
  }
  .contact-list { list-style: none; margin-top: 62px; }
  .contact-list li {
    display: flex; align-items: center; gap: 16px;
    font-size: 21px; line-height: 1.2; margin-bottom: 8px;
  }
  .contact-list li.gap-before { margin-top: 34px; }
  .contact-list li.address { align-items: flex-start; }
  .icon { width: 18px; height: 18px; flex: none; fill: none; stroke: var(--text-soft); stroke-width: 1.6; }
  .icon.solid { fill: var(--text-soft); stroke: none; }
</style>
</head>
<body>
<main class="canvas">
  <article class="card">
    <div class="brand">
      <span class="brand-mark"></span>
      <span class="brand-name">Orla Property<br>Development</span>
    </div>

    <section class="details">
      <h1 class="person-name">Darren Ashcombe</h1>
      <p class="person-role">Managing Director</p>

      <ul class="contact-list">
        <li>
          <svg class="icon" viewBox="0 0 18 18"><rect x="5" y="1.5" width="8" height="15" rx="1.5"/><line x1="8" y1="14" x2="10" y2="14"/></svg>
          +61 438 615 207
        </li>
        <li>
          <svg class="icon" viewBox="0 0 18 18"><path d="M4 2l3 3-1.5 2c1 2 3 4 5 5l2-1.5 3 3-2 2C8 15 3 10 2 4z"/></svg>
          +61 3 8276 4139
        </li>
        <li>
          <svg class="icon" viewBox="0 0 18 18"><rect x="1.5" y="4" width="15" height="10"/><polyline points="1.5,4 9,10 16.5,4"/></svg>
          darren@orla.properties
        </li>
        <li class="gap-before address">
          <svg class="icon solid" viewBox="0 0 18 18"><path d="M9 1a5.5 5.5 0 0 0-5.5 5.5C3.5 11 9 17 9 17s5.5-6 5.5-10.5A5.5 5.5 0 0 0 9 1zm0 7.5a2 2 0 1 1 0-4 2 2 0 0 1 0 4z"/></svg>
          <span>PO BOX 73 Bentleigh,<br>VIC 3024</span>
        </li>
        <li class="gap-before">
          <svg class="icon" viewBox="0 0 18 18"><circle cx="9" cy="9" r="7.5"/><ellipse cx="9" cy="9" rx="3.2" ry="7.5"/><line x1="1.5" y1="9" x2="16.5" y2="9"/></svg>
          www.orla.properties
        </li>
      </ul>
    </section>
  </article>
</main>
</body>
</html>
```